Stationary and Business Card for Law Firm
Modern, Professional & Sophisticated Law Firm Card
Stationary and Business Card for Law Firm - Law
Creative Brief
Professional
Owen Barker
Partner
482 North Mill Avenue Pelham, Illinois 62904
obarker@barkerwynn.example
www.barkerwynn.example
These cards will be used by three attorneys, so I would like to be able to change the names out. Alternatively, if you could insert the names when providing source files, it would be appreciated. Names are: Owen B. Barker Rosalind P. Barker Natalie K. Wynn Emails are: obarker@barkerwynn.example rbarker@barkerwynn.example nwynn@barkerwynn.example
pbruner27 pbruner27
While I like the look many of the envelopes, the return address must be in the upper right hand corner to meet US Postal regulations. Firm Name/Logo Address City, State Zip (additional design info if you like) I have had similar envelopes on a different project with the Logo address on the lower part of the envelope---the post office refused to accept them.

```html
<!DOCTYPE html>
<html lang="en">
<head>
<meta charset="utf-8">
<title>Barker &amp; Wynn — Business Card</title>
<link rel="stylesheet" href="https://fonts.googleapis.com/css2?family=Cormorant+Garamond:wght@500;600&family=Work+Sans:wght@400;500&display=swap">
<style>
  :root {
    --backdrop: #e8e8e8;
    --card-front: #ffffff;
    --card-back: #2b2a29;
    --gold: #9c8468;
    --ink: #2e2d2c;
    --muted: #555;
    --rule: #b9ab98;
    --white: #ffffff;
  }
  * { margin: 0; padding: 0; box-sizing: border-box; }
  html, body {
    width: 1200px; height: 897px; overflow: hidden;
    background: var(--backdrop);
  }
  .stage { position: relative; width: 1200px; height: 897px; }
  .card {
    position: absolute; left: 330px; width: 543px; height: 308px;
    text-align: center;
    box-shadow: 0 6px 14px rgba(0,0,0,0.12);
  }
  .card--front { top: 109px; background: var(--card-front); color: var(--ink); }
  .card--back  { top: 480px; background: var(--card-back); color: var(--white); }

  .brand-mark {
    position: absolute; left: 243px; top: 19px;
    width: 56px; height: 56px; background: var(--gold);
  }
  .firm-name {
    font-family: "Cormorant Garamond", serif; font-weight: 600;
    text-transform: uppercase; letter-spacing: 0.02em;
  }
  .firm-tagline {
    font-family: "Cormorant Garamond", serif; font-weight: 500;
    text-transform: uppercase; letter-spacing: 0.06em;
  }
  .card--front .firm-name { position: absolute; left: 0; right: 0; top: 90px; font-size: 27px; }
  .card--front .firm-tagline { position: absolute; left: 0; right: 0; top: 121px; font-size: 11px; }

  .person-name {
    position: absolute; left: 0; right: 0; top: 160px;
    font-family: "Cormorant Garamond", serif; font-weight: 600;
    font-size: 25px; color: var(--gold); letter-spacing: 0.04em; text-transform: uppercase;
  }
  .person-title {
    position: absolute; left: 0; right: 0; top: 190px;
    font-family: "Work Sans", sans-serif; font-size: 11px; color: var(--muted);
  }
  .divider {
    position: absolute; left: 153px; width: 237px; top: 215px;
    border-top: 1px solid var(--rule);
  }
  .contact {
    position: absolute; left: 0; right: 0; top: 235px;
    font-family: "Work Sans", sans-serif; font-size: 11.5px; line-height: 19.5px;
    color: var(--ink); list-style: none;
  }
  .contact .label { color: var(--gold); font-weight: 500; }

  .card--back .firm-name { position: absolute; left: 0; right: 0; top: 118px; font-size: 45px; font-weight: 500; }
  .card--back .firm-tagline { position: absolute; left: 0; right: 0; top: 166px; font-size: 16px; }
  .card--back .web {
    position: absolute; left: 0; right: 0; top: 272px;
    font-family: "Work Sans", sans-serif; font-size: 12.5px;
  }
</style>
</head>
<body>
<main class="stage">
  <section class="card card--front">
    <div class="brand-mark"></div>
    <h1 class="firm-name">Barker &amp; Wynn</h1>
    <p class="firm-tagline">Attorneys at Law</p>
    <h2 class="person-name">Owen Barker</h2>
    <p class="person-title">Partner</p>
    <div class="divider"></div>
    <ul class="contact">
      <li><span class="label">P</span> : 217.555.0142 | <span class="label">F</span> : 217.555.0187</li>
      <li><span class="label">E</span> : obarker@barkerwynn.example | <span class="label">W</span> : www.barkerwynn.example</li>
      <li><span class="label">A</span> : 482 North Mill Avenue Pelham, Illinois 62904</li>
    </ul>
  </section>

  <section class="card card--back">
    <h2 class="firm-name">Barker &amp; Wynn</h2>
    <p class="firm-tagline">Attorneys at Law</p>
    <p class="web">www.barkerwynn.example</p>
  </section>
</main>
</body>
</html>
```